Animal Eye Clinic needs a Business card

We are a new veterinary ophthalmology practice (Tessaly Animal Eye Care) and we need a business card designed. We only see animal eyes - we are not a regular veterinary clinic. We already have a logo. We are looking for a professional, good looking business card to hand out to our clients. We are looking for something simple but professional and contemporary. Our logo is likely the only picture/graphic that needs to be on the card.
Updates

Contact Information for Business Card

Marisol Dunkley, BSc, DVM, MSc, DipACVO
Veterinary Ophthalmologist

Phone: 555.418.3097
Email: tessalyanimaleyecare@mailbrook.net
Website: tessalyanimaleyecare.net
Address: 1840 Pellworth Rd
Harlow Bay, NS, B4T 8M3

Colors

Designer to choose colors to be used in the design.

Requirements
Must have
• Our logo (attached)

```html
<!DOCTYPE html>
<html lang="en">
<head>
<meta charset="utf-8">
<title>Tessaly Animal Eye Care – Business Card</title>
<link href="https://fonts.googleapis.com/css2?family=Roboto:wght@400;500;700&display=swap" rel="stylesheet">
<style>
  :root {
    --teal: #1b98a6;
    --teal-faint: #e4f1f3;
    --ink: #4a4a4a;
    --paper: #ffffff;
    --backdrop: #d9dcdf;
  }
  * { margin: 0; padding: 0; box-sizing: border-box; }
  html, body { width: 1200px; height: 800px; overflow: hidden; }
  body {
    background: var(--backdrop);
    font-family: "Roboto", Arial, sans-serif;
    position: relative;
  }
  .card {
    position: absolute;
    left: 300px;
    width: 600px;
    height: 343px;
    background: var(--paper);
    overflow: hidden;
    box-shadow: 0 4px 14px rgba(0,0,0,0.12);
  }
  .card--front { top: 40px; }
  .card--back { top: 417px; }

  .brand {
    position: absolute;
    display: flex;
    align-items: center;
    gap: 12px;
    color: var(--teal);
    font-weight: 700;
    white-space: nowrap;
  }
  .brand__dot {
    width: 34px; height: 34px;
    border-radius: 50%;
    background: var(--teal);
    flex: none;
  }
  .brand__name { font-size: 27px; letter-spacing: 0.2px; }

  .card--front .brand { left: 110px; top: 128px; z-index: 2; }
  .front__web {
    position: absolute;
    left: 112px; top: 236px;
    color: var(--teal);
    font-size: 15px;
    letter-spacing: 1.6px;
    z-index: 2;
  }
  .front__art { position: absolute; right: 0; top: 0; }

  .back__art { position: absolute; left: 0; top: 0; }
  .card--back .brand { right: 34px; top: 42px; }
  .card--back .brand__name { font-size: 25px; }

  .contact {
    position: absolute;
    right: 34px; top: 102px;
    text-align: right;
    color: var(--ink);
  }
  .contact__name {
    color: var(--teal);
    font-weight: 700;
    font-size: 19px;
    letter-spacing: 0.3px;
  }
  .contact__creds { font-size: 13px; }
  .contact__title { font-size: 16px; margin-top: 2px; }
  .contact__address { font-size: 16px; line-height: 1.3; margin-top: 14px; }
  .contact__lines { list-style: none; font-size: 16px; line-height: 1.35; margin-top: 6px; }
  .contact__lines li { display: flex; justify-content: flex-end; align-items: center; gap: 6px; }
  .icon { width: 14px; height: 14px; fill: none; stroke: var(--teal); stroke-width: 1.6; flex: none; }
</style>
</head>
<body>

<section class="card card--front" aria-label="Card front">
  <svg class="front__art" width="330" height="343" viewBox="0 0 330 343" role="img" aria-label="Faint silhouettes of a horse, dog and cat">
    <path d="M330 0 V343 H40 C60 280 90 230 140 200 C180 170 200 110 230 60 C250 30 280 10 330 0 Z" fill="var(--teal-faint)"/>
  </svg>
  <div class="brand">
    <span class="brand__dot"></span>
    <span class="brand__name">Tessaly Animal Eye Care</span>
  </div>
  <p class="front__web">tessalyanimaleyecare.net</p>
</section>

<section class="card card--back" aria-label="Card back">
  <svg class="back__art" width="250" height="343" viewBox="0 0 250 343" role="img" aria-label="Teal illustration of a horse, dog and cat">
    <path d="M0 0 H150 C120 60 90 110 60 150 C40 180 70 220 120 230 C170 240 210 260 230 300 C240 320 240 335 238 343 H0 Z" fill="var(--teal)"/>
  </svg>
  <div class="brand">
    <span class="brand__dot"></span>
    <span class="brand__name">Tessaly Animal Eye Care</span>
  </div>
  <div class="contact">
    <p class="contact__name">MARISOL DUNKLEY <span class="contact__creds">BSc, DVM, MSc, DipACVO</span></p>
    <p class="contact__title">Veterinary Ophthalmologist</p>
    <p class="contact__address">1840 Pellworth Rd<br>Harlow Bay, NS, B4T 8M3</p>
    <ul class="contact__lines">
      <li>555.418.3097
        <svg class="icon" viewBox="0 0 16 16"><path d="M3 2 L6 2 L7 5 L5 6 C6 8 8 10 10 11 L11 9 L14 10 L14 13 C8 14 2 8 3 2 Z"/></svg></li>
      <li>tessalyanimaleyecare@mailbrook.net
        <svg class="icon" viewBox="0 0 16 16"><rect x="1.5" y="3.5" width="13" height="9"/><path d="M1.5 3.5 L8 9 L14.5 3.5"/></svg></li>
      <li>tessalyanimaleyecare.net
        <svg class="icon" viewBox="0 0 16 16"><circle cx="8" cy="8" r="6.3"/><path d="M1.7 8 H14.3 M8 1.7 C5 5 5 11 8 14.3 M8 1.7 C11 5 11 11 8 14.3"/></svg></li>
    </ul>
  </div>
</section>

</body>
</html>
```